Nutritional neuroscience book cover design*

We need a book cover design for a new book on nutritional neuroscience and aging. The book is written for the general public and answers questions such as, "We are living longer than ever. The problem is, will our brain stay healthy as we age? We certainly do not want to live longer with various diseases, in particular brain diseases. How does the brain change during aging? And what can we do to promote the health of our brain and prevent and treat neurological diseases that typically occur during the aging process?" Based on recent discoveries in the field of nutritional neuroscience, this book presents how we can use nutrition to help our brain stay healthy longer. While our brain shrinks and becomes functionally weaker during the aging process, nutrition is able to slow this process down. This book illustrates this point through chapters on stroke, Parkinson’s disease, Multiple Sclerosis, dementia, depression, anxiety, and schizophrenia. The book will appeal to anyone looking to optimize their brain’s health and performance today and decades into the future.

Target Market(s)

General audience

Colors

Designer to choose colors to be used in the design.

Requirements
Must have
• Title: Meals Across the Decades: A Field Guide to Diet and the Mind
• Edited by Corinne T. Halvorsen, Ph.D.
• Book size: 7*10 inches
• Backcover text:
• Humans are living longer than ever. How does the brain change during aging? Will our brain stay healthy as we age? We certainly do not want to live longer with neurological diseases. What can we do to promote the health of our brain?
• Based on recent discoveries in the field of nutritional neuroscience, this book presents how nutrition affects our brain health. While we age, our brain shrinks and there are changes in how it functions, nutrition is an important component that can help maintain optimal brain health.
• Using scientific evidence, this book illustrates the importance of nutrition for neurological diseases including Alzheimer’s disease, stroke, Parkinson’s disease, Multiple Sclerosis, vascular dementia, depression, anxiety, and schizophrenia. This book will appeal to anyone looking to learn more about how nutrition affects brain health.

```html
<!DOCTYPE html>
<html lang="en">
<head>
<meta charset="UTF-8">
<title>Meals Across the Decades — Book Cover</title>
<link rel="stylesheet" href="https://fonts.googleapis.com/css2?family=Montserrat:wght@400;500;800&family=Kaushan+Script&display=swap">
<style>
  :root {
    --page-bg: #ffffff;
    --cover-dark: #2f3032;
    --cover-mid: #4a4b4e;
    --glow: #6d6e72;
    --white: #ffffff;
    --orange: #f7901e;
    --green: #8dc63f;
    --yellow: #f5e43a;
    --leaf: #5e9a2c;
    --leaf-deep: #2f5a1a;
  }
  * { margin: 0; padding: 0; box-sizing: border-box; }
  html, body {
    width: 1200px; height: 1000px; overflow: hidden;
    background: var(--page-bg);
  }
  .canvas {
    position: relative; width: 1200px; height: 1000px;
  }
  .book-cover {
    position: absolute; left: 285px; top: 50px;
    width: 630px; height: 900px;
    background:
      radial-gradient(ellipse 60% 45% at 55% 45%, var(--glow) 0%, var(--cover-mid) 45%, var(--cover-dark) 100%);
    overflow: hidden;
    font-family: "Montserrat", sans-serif;
    color: var(--white);
    text-align: center;
  }
  .editor {
    position: absolute; top: 125px; left: 0; right: 0;
  }
  .editor-label {
    font-size: 18px; font-weight: 500; letter-spacing: 1px;
  }
  .editor-name {
    margin-top: 14px;
    font-size: 33px; font-weight: 400; letter-spacing: 1.5px;
  }
  .cover-art {
    position: absolute; left: 95px; top: 200px;
    width: 460px; height: 500px;
    border-radius: 48% 48% 32% 30%;
    background:
      radial-gradient(ellipse 42% 34% at 62% 30%, var(--green) 0%, var(--leaf) 45%, var(--leaf-deep) 75%, transparent 100%),
      radial-gradient(ellipse 60% 60% at 55% 50%, #1f2022 0%, #1f2022 60%, transparent 100%);
  }
  .title {
    position: absolute; left: 0; right: 0; top: 500px;
  }
  .title-script {
    font-family: "Kaushan Script", cursive;
    font-size: 48px; line-height: 1;
    text-shadow: 0 2px 6px rgba(0,0,0,0.5);
  }
  .title-main {
    font-size: 84px; font-weight: 800; line-height: 1;
    color: var(--orange); margin-top: 6px;
    letter-spacing: 1px;
  }
  .title-line {
    font-size: 64px; font-weight: 800; line-height: 1;
    margin-top: 4px;
  }
  .title-line .green { color: var(--green); }
  .title-line .yellow { color: var(--yellow); }
  .subtitle {
    margin-top: 16px;
    font-size: 25px; font-weight: 400; line-height: 1.15;
    letter-spacing: 1px;
  }
</style>
</head>
<body>
  <div class="canvas">
    <section class="book-cover">
      <div class="editor">
        <p class="editor-label">EDITED BY</p>
        <p class="editor-name">CORINNE T. HALVORSEN</p>
      </div>

      <div class="cover-art" role="img" aria-label="Dark silhouette of a head in profile with a head of broccoli in place of the brain"></div>

      <h1 class="title">
        <span class="title-script" style="display:block">Meals</span>
        <span class="title-main" style="display:block">ACROSS</span>
        <span class="title-line" style="display:block"><span class="green">THE</span> <span class="yellow">DECADES</span></span>
        <span class="subtitle" style="display:block">A FIELD GUIDE TO DIET<br>AND THE MIND</span>
      </h1>
    </section>
  </div>
</body>
</html>
```